fFable Swap Poker

I'm launching an additional Fable Swap game. It will be similar to the card edition game you already as follows:
1) Box (similar design as previous ones, but black/gold for poker theme)
2) 52 custom twist cards
3) 52 standard deck of cards (nothing to design here)
Attached are the details for the box and cards. I'm also attaching a copy of the template provided by the manufacturer.
Let me know

```html
<!DOCTYPE html>
<html lang="en">
<head>
<meta charset="utf-8">
<title>Fable Swap Poker – Box Front</title>
<link rel="stylesheet" href="https://fonts.googleapis.com/css2?family=Montserrat:wght@600;700&display=swap">
<style>
  :root {
    --stage: #f2f2f2;
    --box-black: #141414;
    --gold: #c9a24a;
    --gold-light: #e6cf8f;
    --gold-soft: #dcc190;
    --panel-white: #ffffff;
    --ink: #111111;
    --logo-blue: #6ea6d6;
  }
  html, body {
    margin: 0;
    width: 1200px;
    height: 1000px;
    overflow: hidden;
    background: var(--stage);
    font-family: "Montserrat", sans-serif;
  }
  .canvas {
    width: 1200px;
    height: 1000px;
    display: flex;
    align-items: center;
    justify-content: center;
  }
  .box-front {
    position: relative;
    width: 580px;
    height: 860px;
    background: var(--box-black);
    border: 6px solid var(--gold);
    border-radius: 6px;
    box-sizing: border-box;
    padding: 26px;
  }
  .front-panel {
    position: relative;
    width: 100%;
    height: 100%;
    border: 8px solid var(--gold);
    border-radius: 48px;
    box-sizing: border-box;
    overflow: hidden;
    background: var(--panel-white);
  }
  .sunburst {
    position: absolute;
    inset: 0;
    background: radial-gradient(circle at 50% 58%, var(--panel-white) 0%, #f7efdd 45%, var(--gold-soft) 100%);
  }
  .panel-content {
    position: relative;
    height: 100%;
    display: flex;
    flex-direction: column;
    align-items: center;
    text-align: center;
  }
  .tagline {
    margin: 64px 0 0;
    font-weight: 700;
    font-size: 36px;
    line-height: 1.25;
    letter-spacing: 4px;
    color: var(--ink);
    text-transform: uppercase;
  }
  .brand-name {
    margin-top: 170px;
    display: flex;
    align-items: center;
    gap: 16px;
    font-weight: 700;
    font-size: 64px;
    color: var(--logo-blue);
  }
  .brand-dot {
    width: 22px;
    height: 22px;
    border-radius: 50%;
    background: var(--logo-blue);
  }
  .game-facts {
    position: absolute;
    bottom: 50px;
    left: 0;
    right: 0;
    display: flex;
    justify-content: center;
    gap: 20px;
    margin: 0;
    padding: 0;
    list-style: none;
    font-weight: 600;
    font-size: 24px;
    color: var(--ink);
  }
  .game-facts li {
    display: flex;
    align-items: center;
    gap: 10px;
  }
  .game-facts li::before {
    content: "";
    width: 9px;
    height: 9px;
    border-radius: 50%;
    background: var(--gold);
  }
</style>
</head>
<body>
  <main class="canvas">
    <section class="box-front">
      <div class="front-panel">
        <div class="sunburst" role="img" aria-label="Gold and white sunburst rays radiating from the centre of the panel"></div>
        <div class="panel-content">
          <h1 class="tagline">Poker with a<br>hilarious twist</h1>
          <div class="brand-name"><span class="brand-dot"></span>Fable Swap</div>
          <ul class="game-facts">
            <li>Family</li>
            <li>Ages 8+</li>
            <li>2-6Players</li>
          </ul>
        </div>
      </div>
    </section>
  </main>
</body>
</html>
```